CREATE A KILLER WEBSITE DESIGN

We are a firearms training company that trains CIVILIANS (no police or military pictures - thank you!) to defend themselves and are looking for a killer design that's clean, easy to navigate and modern! We want the newest trends applied to this sight like a scrollable site so you can scroll down and see all the features. We are okay with tweaking the HTML but need the artistic design to look good. I'll provide a link to our current site along with a sight we really like so you can get an idea!

I'm supplying a PowerPoint Design we are going with from another designer so you can match the style to the new site.

PAGES: (Please use information from our current site. We like the information but just want a more polished look similar to the NWDLA site below but in our colors.)
Home - Long Form Scrolling Site. Top fold will be a video with a play button.
Falcon Institute - Seven Level Training Program Info Page That Will Contain A Video.
Contact Us - This will be a page that DOES NOT CONTAIN AN EMAIL ADDRESS. Just a contact us form
Meet The Trainer: Morgan Pellbrook

Our site:
https://www.brisklanewardens.biz

Sights We Like:
https://www.nwdefenseleague.example.com
https://quorvel.example.com
https://brantforgeworks.example.com
https://www.pelnrigear.example.com

Target Market(s)

Men and women ages 21 to 100 years old

Industry/Entity Type

Self Defense

Number of Pages Required

5+ page

Font styles to use
Sans Serif

Colors
f26267

Requirements
Must have
• Clean and engaging. Use of colors that match our logo.
Should not have
• Poor design quality

```html
<!DOCTYPE html>
<html lang="en">
<head>
<meta charset="utf-8">
<title>Falcon Institute — Concealed Carry Training</title>
<link rel="stylesheet" href="https://fonts.googleapis.com/css2?family=Roboto:wght@400;500;700&family=Saira:wght@700;800&family=Saira+Condensed:wght@700;800&display=swap">
<style>
:root{
  --red:#e3202a;
  --red-dark:#b5151d;
  --ink:#232323;
  --body:#6a6a6a;
  --muted:#9a9a9a;
  --dark:#1f1f1f;
  --darker:#171717;
  --field:#f4f4f4;
  --white:#ffffff;
}
*{box-sizing:border-box;margin:0;padding:0}
html,body{width:1200px;height:4942px;overflow:hidden}
body{position:relative;background:var(--white);font-family:"Roboto",sans-serif;color:var(--body)}
.abs{position:absolute}
.display{font-family:"Saira",sans-serif;font-weight:800;color:var(--ink);letter-spacing:4px;text-transform:uppercase}
.cond{font-family:"Saira Condensed",sans-serif;font-weight:800;text-transform:uppercase}
.eyebrow{font-family:"Roboto",sans-serif;font-weight:700;font-size:13px;color:var(--red);text-transform:uppercase;letter-spacing:.3px}
.btn{position:absolute;display:flex;align-items:center;justify-content:center;background:var(--red);color:var(--white);font-family:"Roboto",sans-serif;font-weight:500;font-size:12.5px;text-transform:uppercase;clip-path:polygon(9px 0,100% 0,calc(100% - 9px) 100%,0 100%)}
.red{color:var(--red)}

/* header + hero */
.hero{position:absolute;left:0;top:0;width:1200px;height:672px;background:linear-gradient(100deg,#2c2b2a 0%,#3b3836 38%,#4a4540 58%,#2f2c29 80%,#1d1c1b 100%)}
.hero-photo{position:absolute;left:0;top:154px;width:1200px;height:512px;background:radial-gradient(ellipse at 72% 55%,#6a5f52 0%,#4a433c 35%,#2d2a27 75%)}
.topbar{position:absolute;left:0;top:0;width:1200px;height:154px;background:linear-gradient(180deg,#1f1e1d 0%,rgba(31,30,29,.85) 100%)}
.brand{position:absolute;left:58px;top:30px;display:flex;align-items:center;gap:14px}
.brand-mark{width:44px;height:44px;border-radius:50%;background:var(--red)}
.brand-name{font-family:"Saira",sans-serif;font-weight:800;font-size:25px;color:var(--white);letter-spacing:2px;line-height:1}
.news{left:490px;top:23px;font-size:11.5px;color:#d6d6d6}
.news-arrow{left:1124px;top:20px;width:20px;height:20px;border:1px solid #777;border-radius:50%}
.signin{left:776px;top:64px;display:flex;align-items:center;gap:10px;color:var(--white);font-size:10.5px;line-height:1.25}
.signin-icon{width:24px;height:24px;border:1.5px solid #cfcfcf;border-radius:50%}
.urgent{left:931px;top:60px;width:202px;height:36px;font-size:11.5px;clip-path:none}
.nav{position:absolute;left:100px;top:118px;display:flex;gap:31px;font-size:13px;font-weight:500;color:var(--white);text-transform:uppercase}
.hero-title{left:58px;top:282px;font-size:38px;line-height:44px;color:var(--white);letter-spacing:.5px}
.hero-btn{left:61px;top:474px;width:160px;height:37px}
.play{left:885px;top:328px}
.hero-rule{position:absolute;left:0;top:666px;width:1200px;height:6px;background:var(--red)}

/* about */
.about-eyebrow{left:61px;top:768px}
.about-name{left:61px;top:790px;font-size:34px}
.portrait{left:62px;top:872px;width:330px;height:330px;border-radius:50%;background:radial-gradient(circle at 50% 40%,#d2d2d2 0%,#9c9c9c 45%,#5b5b5b 100%);border:4px solid #2b2b2b}
.about-copy{left:490px;top:766px;width:652px;font-size:13px;line-height:26.2px;color:#6b6b6b}
.about-copy p+p{margin-top:26px}
.about-copy b{color:var(--ink);font-weight:700}

/* featured */
.featured-eyebrow{left:61px;top:1344px}
.featured-title{left:61px;top:1366px;font-size:34px}
.outlets{position:absolute;left:492px;top:1330px;width:650px;height:90px;display:flex;align-items:center;justify-content:space-between}
.outlet{display:flex;align-items:center;gap:8px;font-family:"Roboto",sans-serif;font-weight:700;font-size:19px;color:#6e6e6e;text-transform:uppercase}
.outlet i{display:block;width:26px;height:26px;background:#6e6e6e}
.outlet i.round{border-radius:50%}

/* levels */
.levels{position:absolute;left:0;top:1497px;width:1200px;height:1623px;background:linear-gradient(180deg,#262626 0%,#383838 40%,#3a3a3a 60%,#242424 100%)}
.levels-title{position:absolute;left:0;top:74px;width:1200px;text-align:center;font-size:38px;line-height:44px;color:var(--white);letter-spacing:1px}
.levels-title svg{position:absolute;left:648px;top:86px}
.levels-intro{position:absolute;left:58px;top:220px;width:1084px;font-size:13.5px;line-height:26px;color:#dedede}
.levels-intro p+p{margin-top:26px}
.level{position:absolute;left:0;width:1200px;height:142px}
.level svg{position:absolute;left:0;top:0}
.level-tag{position:absolute;top:18px;width:120px}
.level-tag .lbl{display:block;font-family:"Saira",sans-serif;font-weight:700;font-size:19px;letter-spacing:3px;color:#8a8a8a;line-height:20px}
.level-tag .num{display:block;font-family:"Saira Condensed",sans-serif;font-weight:800;font-size:66px;line-height:60px;color:var(--red)}
.level h3{position:absolute;top:26px;font-family:"Saira",sans-serif;font-weight:700;font-size:18px;color:var(--white);letter-spacing:.6px;text-transform:uppercase}
.level p{position:absolute;top:64px;width:640px;font-size:13.5px;line-height:27px;color:#e4e4e4}
.level.odd .level-tag{left:226px}
.level.odd h3,.level.odd p{left:344px}
.level.even .level-tag{left:925px}
.level.even h3{right:336px;text-align:right}
.level.even p{right:336px;text-align:right}
.levels-cta-link{left:490px;top:1521px;width:84px;font-size:12.5px;font-weight:500;color:var(--white)}
.levels-cta{left:618px;top:1514px;width:176px;height:36px}

/* testimonials */
.t-eyebrow{left:61px;top:3198px}
.t-title{left:61px;top:3222px;font-size:38px;letter-spacing:5px}
.quote{position:absolute;top:3325px;width:262px}
.quote h4{font-family:"Roboto",sans-serif;font-weight:700;font-size:13.5px;line-height:21px;color:var(--ink);text-transform:uppercase}
.quote p{margin-top:18px;font-size:14px;line-height:26.4px;color:#8a8a8a}
.quote .meta{display:flex;justify-content:space-between;align-items:center;margin-top:16px;font-size:10.5px;color:#9a9a9a}
.quote .meta b{font-size:12.5px;color:var(--ink);font-weight:700}
.slider{position:absolute;left:86px;top:3642px;width:1056px;height:3px;background:#d6d6d6}
.slider span{position:absolute;left:0;top:-1px;width:173px;height:5px;background:var(--red)}

/* contact */
.contact-band{position:absolute;left:0;top:3802px;width:518px;height:518px;background:var(--red)}
.contact-photo{position:absolute;left:67px;top:3725px;width:510px;height:595px;background:linear-gradient(160deg,#c9b6a2 0%,#8f7a62 40%,#5d5a3c 70%,#3c3a2a 100%);clip-path:polygon(22% 0,70% 0,100% 40%,100% 100%,0 100%,0 30%)}
.c-eyebrow{left:599px;top:3826px}
.c-title{left:599px;top:3848px;font-size:34px;line-height:45px}
.field{position:absolute;left:601px;width:459px;background:var(--field);display:flex;align-items:flex-start;gap:16px;padding:20px 0 0 30px;font-size:14px;color:#9a9a9a}
.field svg{flex:none}
.send{left:908px;top:4254px;width:152px;height:39px}

/* footer */
.footer{position:absolute;left:0;top:4320px;width:1200px;height:622px;background:var(--dark)}
.f-brand{position:absolute;left:58px;top:50px;display:flex;align-items:center;gap:12px}
.f-brand .brand-mark{width:36px;height:36px}
.f-brand .brand-name{font-size:20px}
.nl-title{left:323px;top:64px;font-family:"Saira",sans-serif;font-weight:800;font-size:19px;color:var(--white);letter-spacing:.5px}
.nl-copy{left:323px;top:98px;font-size:12.5px;line-height:21px;color:#cfcfcf}
.nl-input{left:716px;top:82px;width:290px;height:48px;background:#2d2d2d;padding:16px 0 0 30px;font-size:13px;color:#9a9a9a}
.nl-btn{left:994px;top:82px;width:146px;height:48px;font-size:13px}
.f-rule{position:absolute;left:0;top:192px;width:1200px;height:1px;background:#3a3a3a}
.f-col{position:absolute;top:244px}
.f-col h5{font-family:"Roboto",sans-serif;font-weight:700;font-size:13px;color:var(--red);text-transform:uppercase;margin-bottom:10px}
.f-col li{list-style:none;font-size:13px;line-height:27px;color:#e2e2e2}
.social{display:flex;gap:10px;flex-wrap:wrap;width:200px}
.social span{display:flex;align-items:center;gap:5px;font-size:11.5px;color:#e2e2e2}
.social i{display:block;width:10px;height:10px;background:#e2e2e2}
.card{position:absolute;left:58px;top:442px;width:1084px;height:124px;background:var(--white)}
.card-name{left:82px;top:26px;font-family:"Saira",sans-serif;font-weight:800;font-size:19px;color:var(--ink);letter-spacing:1.5px}
.card-role{left:82px;top:56px;font-size:11.5px;line-height:15px;color:#8a8a8a;text-transform:uppercase;width:330px}
.card-line{display:flex;gap:10px;font-size:12px;line-height:15px;color:#8a8a8a;text-transform:uppercase}
.card-line svg{flex:none;margin-top:2px}
.copyright{position:absolute;left:0;top:590px;width:1200px;text-align:center;font-size:11.5px;color:#d8d8d8}
</style>
</head>
<body>

<header class="hero">
  <div class="hero-photo" role="img" aria-label="Photo of a civilian student aiming a handgun at an indoor shooting range"></div>
  <div class="topbar"></div>
  <div class="brand"><span class="brand-mark"></span><span class="brand-name">FALCON INSTITUTE</span></div>
  <div class="abs news">Falcon Institute COVID-19 Response : Lorem ipsum dolor sit amet, consectetur adipiscing elit. Sed ultricies...</div>
  <div class="abs news-arrow"></div>
  <div class="abs signin"><span class="signin-icon"></span><span><b>Sign In</b> or<br>Create An Account</span></div>
  <div class="btn urgent">I need immediate service</div>
  <nav class="nav">
    <span>Home</span><span>Falcon Institute</span><span>Testimonials</span><span>About</span><span>Upcoming Classes</span><span>Shop</span><span>Videos</span><span>Lost Certificate</span><span>Contact Us</span>
  </nav>
  <h1 class="abs cond hero-title">Your life may depend on what<br>you learn in your concealed<br>carry training. <span class="red">Don't settle<br>for a gun shop class!</span></h1>
  <div class="btn hero-btn">Learn more</div>
  <svg class="abs play" width="64" height="64" viewBox="0 0 64 64" aria-label="Play video">
    <circle cx="32" cy="32" r="29" fill="none" stroke="#fff" stroke-width="3"/>
    <path d="M26 20 L45 32 L26 44 Z" fill="#fff"/>
  </svg>
  <div class="hero-rule"></div>
</header>

<section aria-label="About the instructor">
  <div class="abs eyebrow about-eyebrow">About the instructor</div>
  <h2 class="abs display about-name">Morgan Pellbrook</h2>
  <div class="abs portrait" role="img" aria-label="Black and white portrait of instructor Morgan Pellbrook"></div>
  <div class="abs about-copy">
    <p>Morgan Pellbrook is a 3rd generation Jacksonville native and delighted to be a part of this great community. He is a true security expert with <b>25 years of experience in the security industry.</b> He has appeared on <b>Kestrel, Northline, Metro One &amp; Capital 9</b> news outlets. He has been Featured in numerous publications and has trained thousands to protect themselves and their homes from thugs and thieves. He is certified by both the <b>NMSA</b> &amp; the <b>NWDLA</b> as a firearms instructor. He is also an <b>NMSA Range Safety Officer</b> and Defensive Pistol Instructor. He often says: "My students are like family so I take their security personal. I want them to feel confident that they can protect themselves and their families!"</p>
    <p>Ironside Carry is a <b>radically different</b> concealed carry class focusing on the TRUTH about how "Real Attacks" take place. The Concealed Carry Class goes over way more than just the boring, lecture-style, gun shop curriculum into real strategies, tactics and training suggestions to help you prepare! You have to experience it to believe it! We also offer <b>The Falcon Institute</b> for those who are looking for a <b>Fully Immersive, Reality Based training environment</b> that prepares you to <b>defend against the worst threats you may face!</b> In The Institute, we utilize <b>high tech</b>, military/law enforcement grade <b>simulators</b> to <b>take training to a level never before seen in the world of concealed carry.</b></p>
  </div>
</section>

<section aria-label="Featured on">
  <div class="abs eyebrow featured-eyebrow">Our appearances</div>
  <h2 class="abs display featured-title">Featured on</h2>
  <div class="outlets">
    <span class="outlet"><i></i>Kestrel News</span>
    <span class="outlet"><i class="round"></i>Northline</span>
    <span class="outlet">Capital 9 News</span>
    <span class="outlet"><i class="round"></i>Metro One</span>
  </div>
</section>

<section class="levels" aria-label="Seven levels of training">
  <h2 class="cond levels-title">Our 7 levels of training take you<br>from <span class="red">zero to hero</span>
    <svg width="150" height="10" viewBox="0 0 150 10"><path d="M2 8 Q75 0 148 4" fill="none" stroke="#e3202a" stroke-width="2.5"/></svg>
  </h2>
  <div class="levels-intro">
    <p>Wanna hear something funny? Guess what the average person asks about a concealed weapons class? "How much is it and how long is it?" Can you believe it? We are talking about preparing you for life and death situations and the main concern is "How Fast" and "How Cheap?" WOW!</p>
    <p>Why do most people settle for a cheap &amp; quick concealed carry class? It's a fair question! Could you imagine a military soldier trained by a 2-hour class? How effective would they be in the heat of battle? If you want to be ready to SURVIVE an attack, YOU NEED MORE than a basic, run of the mill class! That's why we created a PROPRIETARY 7 LEVEL TRAINING SYSTEM to take you all the way to the peak of readiness!</p>
  </div>

  <svg width="0" height="0" style="position:absolute">
    <defs>
      <linearGradient id="fade-right" gradientUnits="userSpaceOnUse" x1="150" y1="0" x2="1030" y2="0">
        <stop offset="0.5" stop-color="#e3202a"/><stop offset="1" stop-color="#e3202a" stop-opacity="0"/>
      </linearGradient>
      <linearGradient id="fade-left" gradientUnits="userSpaceOnUse" x1="1074" y1="0" x2="180" y2="0">
        <stop offset="0.5" stop-color="#e3202a"/><stop offset="1" stop-color="#e3202a" stop-opacity="0"/>
      </linearGradient>
    </defs>
  </svg>

  <div class="level odd" style="top:456px">
    <svg width="1200" height="142"><path d="M1030 3 H194 L150 71 L194 139 H1030" fill="none" stroke="url(#fade-right)" stroke-width="5"/></svg>
    <div class="level-tag"><span class="lbl">LEVEL</span><span class="num">01</span></div>
    <h3>Concealed carry class</h3>
    <p>Lorem ipsum dolor sit amet, consectetur adipiscing elit. Morbi tincidunt ante ac ultricies<br>vestibulum. Integer sapien magna, ultricies vel fringilla in, fermentum ac arcu.</p>
  </div>
  <div class="level even" style="top:598px">
    <svg width="1200" height="142"><path d="M180 3 H1030 L1074 71 L1030 139 H180" fill="none" stroke="url(#fade-left)" stroke-width="5"/></svg>
    <div class="level-tag"><span class="lbl">LEVEL</span><span class="num">02</span></div>
    <h3>Dynamic defensive shooting</h3>
    <p>Lorem ipsum dolor sit amet, consectetur adipiscing elit. Morbi tincidunt ante ac ultricies<br>vestibulum. Integer sapien magna, ultricies vel fringilla in, fermentum ac arcu.</p>
  </div>
  <div class="level odd" style="top:740px">
    <svg width="1200" height="142"><path d="M1030 3 H194 L150 71 L194 139 H1030" fill="none" stroke="url(#fade-right)" stroke-width="5"/></svg>
    <div class="level-tag"><span class="lbl">LEVEL</span><span class="num">03</span></div>
    <h3>Fine tuning your technique</h3>
    <p>Lorem ipsum dolor sit amet, consectetur adipiscing elit. Morbi tincidunt ante ac ultricies<br>vestibulum. Integer sapien magna, ultricies vel fringilla in, fermentum ac arcu.</p>
  </div>
  <div class="level even" style="top:882px">
    <svg width="1200" height="142"><path d="M180 3 H1030 L1074 71 L1030 139 H180" fill="none" stroke="url(#fade-left)" stroke-width="5"/></svg>
    <div class="level-tag"><span class="lbl">LEVEL</span><span class="num">04</span></div>
    <h3>Virtual threat-lab</h3>
    <p>Lorem ipsum dolor sit amet, consectetur adipiscing elit. Morbi tincidunt ante ac ultricies<br>vestibulum. Integer sapien magna, ultricies vel fringilla in, fermentum ac arcu.</p>
  </div>
  <div class="level odd" style="top:1024px">
    <svg width="1200" height="142"><path d="M1030 3 H194 L150 71 L194 139 H1030" fill="none" stroke="url(#fade-right)" stroke-width="5"/></svg>
    <div class="level-tag"><span class="lbl">LEVEL</span><span class="num">05</span></div>
    <h3>Tactical skills &amp; drills</h3>
    <p>Lorem ipsum dolor sit amet, consectetur adipiscing elit. Morbi tincidunt ante ac ultricies<br>vestibulum. Integer sapien magna, ultricies vel fringilla in, fermentum ac arcu.</p>
  </div>
  <div class="level even" style="top:1166px">
    <svg width="1200" height="142"><path d="M180 3 H1030 L1074 71 L1030 139 H180" fill="none" stroke="url(#fade-left)" stroke-width="5"/></svg>
    <div class="level-tag"><span class="lbl">LEVEL</span><span class="num">06</span></div>
    <h3>Close quarters defense</h3>
    <p>Lorem ipsum dolor sit amet, consectetur adipiscing elit. Morbi tincidunt ante ac ultricies<br>vestibulum. Integer sapien magna, ultricies vel fringilla in, fermentum ac arcu.</p>
  </div>
  <div class="level odd" style="top:1308px">
    <svg width="1200" height="142"><path d="M1030 3 H194 L150 71 L194 139 H1030" fill="none" stroke="url(#fade-right)" stroke-width="5"/></svg>
    <div class="level-tag"><span class="lbl">LEVEL</span><span class="num">07</span></div>
    <h3>Live scenario threat-lab</h3>
    <p>Lorem ipsum dolor sit amet, consectetur adipiscing elit. Morbi tincidunt ante ac ultricies<br>vestibulum. Integer sapien magna, ultricies vel fringilla in, fermentum ac arcu.</p>
  </div>

  <div class="abs levels-cta-link">LEARN MORE</div>
  <div class="btn levels-cta">Enroll today</div>
</section>

<section aria-label="Testimonials">
  <div class="abs eyebrow t-eyebrow">Testimonials</div>
  <h2 class="abs display t-title">Our students' success stories</h2>
  <article class="quote" style="left:102px">
    <h4>My first class was a gun shop class and a waste of money.</h4>
    <p>I've been shooting for years and already had my concealed weapons license. My first class was a gun shop class and a waste of money. Morgan took the time to show me how to properly grip my gun and my shooting dramatically improved!</p>
    <div class="meta"><span>March 3 2018</span><b>- Dale R.</b></div>
  </article>
  <article class="quote" style="left:467px">
    <h4>Thank you Ironside Carry!</h4>
    <p>I had never held a gun when I took the Ironside Carry class and I'm hooked! I'm going all the way to level 7! Thank you Ironside Carry!</p>
    <div class="meta"><span>October 14, 2017</span><b>- Renee K.</b></div>
  </article>
  <article class="quote" style="left:829px">
    <h4>I feel sorry for the next thug that tries me!</h4>
    <p>I was mugged here in Jacksonville and lived in fear ever since. It stole my happiness and I became scared to go out. I'm a Level 4 student and I feel sorry for the next thug that tries me!"</p>
    <div class="meta"><span>December 9, 2017</span><b>- Lorna P.</b></div>
  </article>
  <div class="slider"><span></span></div>
</section>

<section aria-label="Contact us">
  <div class="contact-band"></div>
  <div class="contact-photo" role="img" aria-label="Photo of a woman in ear protection aiming a pistol while an instructor guides her"></div>
  <div class="abs eyebrow c-eyebrow">Contact us</div>
  <h2 class="abs display c-title">Need help? Let our<br>experts guide you.</h2>
  <div class="field" style="top:3974px;height:58px;padding-top:20px">
    <svg width="18" height="18" viewBox="0 0 18 18" fill="none" stroke="#9a9a9a" stroke-width="1.4"><circle cx="9" cy="6" r="3.6"/><path d="M2.5 17c0-3.6 2.9-6 6.5-6s6.5 2.4 6.5 6"/></svg>Name</div>
  <div class="field" style="top:4045px;height:58px">
    <svg width="18" height="18" viewBox="0 0 18 18" fill="none" stroke="#9a9a9a" stroke-width="1.4"><rect x="1.5" y="3.5" width="15" height="11"/><path d="M1.5 3.5 L9 10 L16.5 3.5"/></svg>Email</div>
  <div class="field" style="top:4114px;height:129px">
    <svg width="18" height="18" viewBox="0 0 18 18" fill="none" stroke="#9a9a9a" stroke-width="1.4"><path d="M16.5 1.5 L1.5 8 L7.5 10.5 L10 16.5 Z M7.5 10.5 L16.5 1.5"/></svg>Message</div>
  <div class="btn send">Send</div>
</section>

<footer class="footer">
  <div class="f-brand"><span class="brand-mark"></span><span class="brand-name">FALCON INSTITUTE</span></div>
  <div class="abs nl-title">SUBSCRIBE TO OUR NEWSLETTER!</div>
  <div class="abs nl-copy">Be the first to grab our exclusive offers, promotions<br>and news. Subscribe Today!</div>
  <div class="abs nl-input">Enter your email</div>
  <div class="btn nl-btn">Subscribe</div>
  <div class="f-rule"></div>

  <div class="f-col" style="left:60px"><h5>Quick links</h5>
    <ul><li>Falcon Institute</li><li>Testimonials</li><li>About</li><li>Upcoming Classes</li><li>Shop</li></ul></div>
  <div class="f-col" style="left:271px"><h5>&nbsp;</h5>
    <ul><li>Videos</li><li>Lost Certificate</li><li>Immediate Sign Up</li><li>Contact Us</li></ul></div>
  <div class="f-col" style="left:492px"><h5>My account</h5>
    <ul><li>Sign In</li><li>Create an account</li></ul></div>
  <div class="f-col" style="left:703px"><h5>Terms &amp; conditions</h5>
    <ul><li>Privacy Policy</li><li>Refund Policy</li><li>Terms And Conditions</li><li>Restrictions</li></ul></div>
  <div class="f-col" style="left:964px"><h5>We're on social</h5>
    <div class="social"><span><i></i>Brightfeed</span><span><i></i>Chatter</span><span><i></i>Roster</span><span><i></i>Lens</span></div></div>

  <div class="card">
    <div class="abs card-name">MORGAN PELLBROOK</div>
    <div class="abs card-role">NMSA firearms instructor, NWDLA instructor &amp; training counsellor, news correspondent, and security expert</div>
    <div class="abs card-line" style="left:495px;top:28px">
      <svg width="14" height="14" viewBox="0 0 14 14"><path d="M3 1 L5.5 1 L6.5 4 L5 5.2 C5.8 7 7 8.2 8.8 9 L10 7.5 L13 8.5 L13 11 C13 12 12 13 11 13 C6 12.5 1.5 8 1 3 C1 2 2 1 3 1 Z" fill="#e3202a"/></svg>
      <span>Local: 555-010-4422<br>Toll-free: 800-555-0199</span></div>
    <div class="abs card-line" style="left:495px;top:80px">
      <svg width="14" height="12" viewBox="0 0 14 12"><rect x="0.5" y="1" width="13" height="10" fill="#e3202a"/><path d="M0.5 1 L7 6.5 L13.5 1" fill="none" stroke="#fff" stroke-width="1.2"/></svg>
      <span style="text-transform:none">hello@ironsidecarry.example.com</span></div>
    <div class="abs card-line" style="left:868px;top:28px">
      <svg width="12" height="16" viewBox="0 0 12 16"><path d="M6 0 C2.7 0 0 2.6 0 5.8 C0 10 6 16 6 16 C6 16 12 10 12 5.8 C12 2.6 9.3 0 6 0 Z" fill="#e3202a"/><circle cx="6" cy="6" r="2.2" fill="#fff"/></svg>
      <span>P.O. Box 4410<br>Harbor Point,<br>FL 32990</span></div>
  </div>
  <div class="copyright">©2021 Ironside Carry. All Rights Reserved.</div>
</footer>

</body>
</html>
```